Business card design needed

Double sided
Color, unique, elegant

Maybe put this quote somewhere?? But I think it might make it to cluttered?
“The Pilates Method of Body
Conditioning develops the body
uniformly, corrects posture, restores
vitality, invigorates the mind and
elevates the spirit”
- Henrik Dovacombe

Industry/Entity Type

Business

Contact Information for Business Card

Marta Kellbrook
Pilates Instructor & Personal trainer
Mobile: 0498265043
www.lorvix.com.au
email: lorvixhealth.fitness@qentamail.com

```html
<!DOCTYPE html>
<html lang="en">
<head>
<meta charset="utf-8">
<title>Lorvix Health and Fitness – Business Card</title>
<link rel="stylesheet" href="https://fonts.googleapis.com/css2?family=Questrial&family=Dancing+Script:wght@500&family=Kalam:wght@400&display=swap">
<style>
  :root {
    --backdrop: #1c1c1d;
    --card-pink: #c873b8;
    --card-dark: #2b2b2c;
    --white: #ffffff;
    --ink-pink: #c05aa8;
    --ink-grey: #8a8a8a;
    --quote-green: #a6e07e;
    --author-pink: #e07fcf;
    --stitch-light: rgba(255,255,255,0.75);
    --stitch-dark: rgba(214,120,196,0.7);
  }
  * { box-sizing: border-box; margin: 0; padding: 0; }
  html, body {
    width: 1200px; height: 576px; overflow: hidden;
    background: var(--backdrop);
    font-family: "Questrial", "Century Gothic", sans-serif;
  }
  .canvas {
    position: relative; width: 1200px; height: 576px;
    display: flex; align-items: center; justify-content: center; gap: 60px;
  }
  .card {
    position: relative; width: 500px; height: 290px;
    border-radius: 22px; overflow: hidden;
  }
  .card::after {
    content: ""; position: absolute; inset: 9px;
    border-radius: 15px; border: 1px dashed var(--stitch-light);
    pointer-events: none;
  }
  .card--front { background: var(--card-pink); }
  .card--back { background: var(--card-dark); }
  .card--back::after { border-color: var(--stitch-dark); }

  /* brand block */
  .brand { position: absolute; display: flex; flex-direction: column; align-items: flex-start; color: var(--white); }
  .brand__mark {
    width: 34px; height: 34px; border-radius: 50%;
    border: 2px solid var(--white); margin-bottom: 8px;
  }
  .brand__name { font-size: 30px; letter-spacing: 3px; line-height: 1; }
  .brand__tagline { font-size: 12px; margin-top: 4px; }
  .card--front .brand { left: 40px; top: 78px; }
  .card--back .brand { left: 70px; top: 80px; }
  .card--back .brand__mark { border-color: var(--quote-green); margin-left: 14px; }

  /* name bubble */
  .name-bubble {
    position: absolute; left: 190px; top: 54px;
    width: 280px; height: 62px; background: var(--white);
    border-radius: 10px; padding: 8px 14px 0;
    display: flex; flex-direction: column; align-items: center;
  }
  .name-bubble__tail { position: absolute; left: 4px; bottom: -16px; }
  .name-bubble__name {
    font-family: "Kalam", cursive; font-size: 21px; line-height: 1.15;
    color: var(--ink-pink); white-space: nowrap;
  }
  .name-bubble__role {
    align-self: flex-end; font-size: 10.5px; color: var(--ink-grey);
    margin-top: 2px; white-space: nowrap;
  }

  /* contacts */
  .contacts { position: absolute; left: 180px; top: 160px; list-style: none; color: var(--white); font-size: 13px; }
  .contacts__item { display: flex; align-items: center; gap: 12px; height: 26px; margin-bottom: 4px; white-space: nowrap; }
  .contacts__icon {
    width: 20px; height: 20px; border-radius: 50%; background: var(--white);
    display: flex; align-items: center; justify-content: center; flex: none;
  }

  /* quote */
  .quote { position: absolute; left: 255px; top: 78px; width: 210px; text-align: center; }
  .quote__text {
    font-family: "Dancing Script", cursive; font-size: 15px; line-height: 1.25;
    color: var(--quote-green);
  }
  .quote__author { font-size: 13px; font-weight: 700; color: var(--author-pink); margin-top: 8px; }
</style>
</head>
<body>
<main class="canvas">

  <section class="card card--front" aria-label="Card front">
    <div class="brand">
      <span class="brand__mark"></span>
      <span class="brand__name">LORVIX</span>
      <span class="brand__tagline">Health and Fitness</span>
    </div>

    <div class="name-bubble">
      <svg class="name-bubble__tail" width="22" height="18" viewBox="0 0 22 18" aria-hidden="true">
        <path d="M0 0 L0 18 L20 0 Z" fill="#ffffff"/>
      </svg>
      <p class="name-bubble__name">Marta Kellbrook Pilates</p>
      <p class="name-bubble__role">Instructor &amp; Personal trainer</p>
    </div>

    <ul class="contacts">
      <li class="contacts__item">
        <span class="contacts__icon">
          <svg width="12" height="12" viewBox="0 0 24 24" aria-hidden="true"><path fill="#c873b8" d="M6.6 10.8a15 15 0 0 0 6.6 6.6l2.2-2.2a1 1 0 0 1 1-.25 11.4 11.4 0 0 0 3.6.57 1 1 0 0 1 1 1V20a1 1 0 0 1-1 1A17 17 0 0 1 3 4a1 1 0 0 1 1-1h3.5a1 1 0 0 1 1 1c0 1.250.2 2.450.57 3.570a1 1 0 0 1-.25 1z"/></svg>
        </span>
        <span>0498265043</span>
      </li>
      <li class="contacts__item">
        <span class="contacts__icon">
          <svg width="12" height="12" viewBox="0 0 24 24" aria-hidden="true"><g fill="none" stroke="#c873b8" stroke-width="2"><circle cx="12" cy="12" r="9"/><path d="M3 12h18M12 3c3 3 3 15 0 18M12 3c-3 3-3 15 0 18"/></g></svg>
        </span>
        <span>www.lorvix.com.au</span>
      </li>
      <li class="contacts__item">
        <span class="contacts__icon">
          <svg width="12" height="12" viewBox="0 0 24 24" aria-hidden="true"><g fill="none" stroke="#c873b8" stroke-width="2"><rect x="3" y="6" width="18" height="12" rx="1"/><path d="M3 7l9 6 9-6"/></g></svg>
        </span>
        <span>lorvixhealth.fitness@qentamail.com</span>
      </li>
    </ul>
  </section>

  <section class="card card--back" aria-label="Card back">
    <div class="brand">
      <span class="brand__mark"></span>
      <span class="brand__name">LORVIX</span>
      <span class="brand__tagline">Health and Fitness</span>
    </div>

    <blockquote class="quote">
      <p class="quote__text">“The Pilates Method of Body Conditioning develops the body uniformly, corrects posture, restores vitality, invigorates the mind and elevates the spirit”</p>
      <p class="quote__author">Henrik Dovacombe</p>
    </blockquote>
  </section>

</main>
</body>
</html>
```